Craft Brewery Beer Can Label in Alaska

Design a 16oz can label for a craft brewery.

We are making a can design that can be used for our 6 normal beers. Our desire is to have a standard design but one major element have the color change on each beer type. We included examples of how this works for others.

Elements we general like in designs - mountain scenes, waterfalls, topo map lines, hops. None/all are not required in a design but gives starting options. We are on the ocean in a glacier fjord so think mountains, glaciers and water.

Requirements
Must have
• Company Logo – provided
Frostmark Certified Logo – provided
Freehold Maltsters Logo – provided

Alcohol warning text -

GOVERNMENT WARNING: (1) According to the Surgeon General, women should not drink alcoholic beverages during pregnancy because of the risk of birth defects. (2) Consumption of alcoholic beverages impairs your ability to drive a car or operate machinery, and may cause health problems.

Beer Name – Tide Lantern Pilsner
ABV – 4.9% ABV
Size – 16 FL OZ
Nice to have
• Elements we general like in designs - mountain scenes, waterfalls, topo map lines, hops. None/all are not required in a design but gives starting options. We are on the ocean in a glacier fjord so think mountains, glaciers and water.

```html
<!DOCTYPE html>
<html lang="en">
<head>
<meta charset="utf-8">
<title>Glacierline Brewing – Tide Lantern Pilsner 16 oz Can Label</title>
<link rel="stylesheet" href="https://fonts.googleapis.com/css2?family=Oswald:wght@300;400;600;700&display=swap">
<style>
  :root {
    --navy: #0b1c35;
    --glacier-blue: #0a74bb;
    --ice-blue: #3a95d6;
    --crest-blue: #1466a8;
    --snow: #ffffff;
    --font-condensed: "Oswald", "Arial Narrow", sans-serif;
  }
  * { margin: 0; padding: 0; box-sizing: border-box; }
  html, body { width: 1200px; height: 900px; overflow: hidden; background: #ffffff; }

  .can-label {
    position: absolute; left: 20px; top: 50px;
    width: 1160px; height: 800px;
    background: var(--navy);
    overflow: hidden;
    font-family: var(--font-condensed);
    color: var(--snow);
  }

  .mountain-range {
    position: absolute; left: 0; top: 330px; width: 1160px; height: 250px;
    background: linear-gradient(180deg, var(--ice-blue) 0%, #2b82c4 45%, var(--glacier-blue) 100%);
    clip-path: polygon(0 45%, 8% 30%, 20% 25%, 33% 5%, 44% 0, 55% 12%, 67% 8%, 80% 22%, 92% 30%, 100% 35%, 100% 100%, 0 100%);
  }
  .label-base {
    position: absolute; left: 0; top: 578px; width: 1160px; height: 222px;
    background: var(--glacier-blue);
  }

  .info-field {
    position: absolute; left: 43px; width: 249px; height: 37px;
    background: var(--snow); border-radius: 7px;
    color: var(--navy); font-weight: 600; font-size: 16px;
    line-height: 37px; padding-left: 12px;
  }
  .info-field--abv { top: 83px; }
  .info-field--date { top: 137px; }
  .info-field__value { margin-left: 10px; font-weight: 700; }

  .recycle-note {
    position: absolute; left: 69px; top: 290px; width: 100px;
    text-align: center; font-weight: 300; font-size: 20px; line-height: 1.2;
  }
  .recycle-note svg { display: block; margin: 4px auto; }

  .beer-crest {
    position: absolute; left: 382px; top: 43px; width: 337px; height: 300px; z-index: 2;
  }
  .beer-ribbon {
    position: absolute; left: 368px; top: 180px; width: 408px; height: 100px; z-index: 3;
    background: var(--snow); border-radius: 14px;
    display: flex; align-items: center; justify-content: center;
  }
  .beer-name {
    color: var(--navy); font-weight: 700; font-size: 36px;
    letter-spacing: 1px; text-transform: uppercase; line-height: 1;
  }

  .brand-name {
    position: absolute; text-align: center; font-weight: 700;
    color: var(--snow); text-transform: uppercase; line-height: 1;
  }
  .brand-name--corner { left: 820px; top: 276px; width: 310px; font-size: 46px; }
  .brand-name--corner span { display: block; font-size: 24px; letter-spacing: 14px; margin-top: 8px; padding-left: 14px; }
  .brand-name--main { left: 340px; top: 540px; width: 390px; font-size: 58px; z-index: 4; }
  .brand-name--main span { display: block; font-size: 28px; letter-spacing: 18px; margin-top: 6px; padding-left: 18px; }

  .product-line {
    position: absolute; left: 333px; width: 400px; text-align: center; z-index: 4; line-height: 1;
  }
  .product-line--type { top: 650px; font-size: 42px; font-weight: 600; letter-spacing: 0.5px; }
  .product-line--size { top: 710px; font-size: 26px; font-weight: 600; }

  .cert-badge { position: absolute; background: var(--snow); z-index: 4; }
  .cert-badge--freehold { left: 76px; top: 478px; width: 76px; height: 138px; border-radius: 10px; }
  .cert-badge--frostmark { left: 172px; top: 501px; width: 99px; height: 115px; border-radius: 4px; }

  .brewery-contact {
    position: absolute; left: 80px; top: 644px; z-index: 4;
    font-size: 15px; font-weight: 600; line-height: 26px;
  }
  .social-handle { display: flex; align-items: center; gap: 8px; }
  .social-handle i { width: 15px; height: 15px; background: var(--snow); display: inline-block; border-radius: 3px; }

  .bear-mark {
    position: absolute; left: 282px; top: 690px; width: 80px; height: 46px; z-index: 4;
    background: var(--ice-blue); border-radius: 20px;
  }

  .pregnancy-icon {
    position: absolute; left: 1026px; top: 578px; width: 56px; height: 56px;
    border: 3px solid var(--snow); border-radius: 50%; z-index: 4;
  }

  .government-warning {
    position: absolute; left: 790px; top: 642px; width: 345px; z-index: 4;
    font-size: 13px; font-weight: 300; line-height: 18px;
  }
  .government-warning strong { font-weight: 600; }
</style>
</head>
<body>
  <main class="can-label" aria-label="Tide Lantern Pilsner can label, Glacierline Brewing">
    <div class="mountain-range" role="img" aria-label="Snow-capped fjord mountain range illustration"></div>
    <div class="label-base"></div>

    <div class="info-field info-field--abv">ALC. / VOL.<span class="info-field__value">4.9% ABV</span></div>
    <div class="info-field info-field--date">DATE:</div>

    <div class="recycle-note">
      Be Cool
      <svg width="44" height="40" viewBox="0 0 44 40" aria-hidden="true">
        <g fill="none" stroke="#ffffff" stroke-width="5" stroke-linejoin="round">
          <path d="M16 8 L22 2 L28 10"/>
          <path d="M36 22 L40 30 L30 34"/>
          <path d="M10 34 L4 28 L10 20"/>
        </g>
      </svg>
      &amp; Recycle
    </div>

    <svg class="beer-crest" viewBox="0 0 337 300" role="img" aria-label="Hexagonal crest with brewery emblem and hop">
      <polygon points="168,0 337,85 310,230 168,300 27,230 0,85" fill="#1466a8"/>
    </svg>
    <div class="beer-ribbon" role="img" aria-label="Ribbon banner carrying the beer name">
      <span class="beer-name">Tide Lantern Pilsner</span>
    </div>

    <div class="brand-name brand-name--corner">Glacierline<span>Brewing</span></div>

    <div class="cert-badge cert-badge--freehold" role="img" aria-label="Freehold Maltsters badge"></div>
    <div class="cert-badge cert-badge--frostmark" role="img" aria-label="Frostmark Certified badge"></div>

    <div class="brand-name brand-name--main">Glacierline<span>Brewing</span></div>
    <div class="product-line product-line--type">HANDCRAFTED BEER</div>
    <div class="product-line product-line--size">16 FL OZ</div>

    <div class="brewery-contact">
      <div>Made in: Kestrel Sound, Alaska</div>
      <div class="social-handle"><i></i>@glacierlinebrewing</div>
      <div>www.glacierlinebrewing.com</div>
    </div>
    <div class="bear-mark" role="img" aria-label="Walking bear outline illustration"></div>

    <div class="pregnancy-icon" role="img" aria-label="No drinking while pregnant pictogram"></div>
    <p class="government-warning">
      <strong>GOVERNMENT WARNING:</strong><br>
      (1) According to the Surgeon General, women should not drink alcoholic beverages during pregnancy because of the risk of birth defects.<br>
      (2) Consumption of alcoholic beverages impairs your ability to drive a car or operate machinery, and may cause health problems.
    </p>
  </main>
</body>
</html>
```